Kids Bamboo sun protection clothing

We need a flyer to promote our bamboo sun protection range to parents of kids with sensitive due to illness or skin conditions.
Our clothing is made from bamboo that has been specially knitted for high sun protection but does not use chemicals. The clothing is for everyday wear, to the playground, going for walks, after a swim. Special features such as hoods, high necklines, long sleeves and thumb loops create more coverage but it is not a lycra rash vest. You can see the product at www.lumora-wear.com. We would like this flyer (or postcard) to show parents with children who are sensitive tot he sun that there is an option. Their kids might have albinism, Cancer or severe burns, might be sensitive to the sun or have Eczema. These clothes are natural fabric with styling to help look after their skin in the sun. We would like a soft caring approach.

Target Market(s)

Mums of children who have sensitive skin due to burns, cancer, Eczema or UV sensitivity.

Industry/Entity Type

Health

Font styles to use
Sans Serif

Requirements
Must have
• Point out how it can protect the skin with fabric and design features.
• Be eye catching so if it is in a waiting room at the doctors people will go over to pick it up. Be a soft approach that does not concentrate on the illness.
• Website details
Nice to have
• mention that we also do women's wear
• Please use any images off the website

```html
<!DOCTYPE html>
<html lang="en">
<head>
<meta charset="utf-8">
<title>Lumora Kids Clothing Flyer</title>
<link rel="stylesheet" href="https://fonts.googleapis.com/css2?family=Quicksand:wght@500;600;700&family=Lato:ital,wght@0,700;1,700;1,900&display=swap">
<style>
  :root {
    --orange: #f5a023;
    --orange-deep: #e8850f;
    --orange-light: #fdb94a;
    --charcoal: #2e2e2e;
    --ink: #1f1f1f;
    --white: #ffffff;
    --grey-text: #505050;
    --navy: #2a3a5e;
    --sky: #8db0e8;
    --tape: #f2d43a;
    --tape-dark: #2a2a2a;
  }
  * { margin: 0; padding: 0; box-sizing: border-box; }
  html, body { width: 1200px; height: 902px; overflow: hidden; background: #ffffff; }
  .flyer {
    position: relative; width: 1200px; height: 902px; overflow: hidden;
    background: linear-gradient(100deg, var(--orange-deep) 0%, var(--orange) 40%, var(--orange-light) 100%);
    font-family: 'Lato', Arial, sans-serif;
  }
  .backdrop { position: absolute; inset: 0; }
  .title {
    position: absolute; left: 0; width: 1200px; top: 40px; text-align: center;
    font-family: 'Quicksand', Arial, sans-serif; font-weight: 600; font-size: 86px;
    letter-spacing: 1px; color: var(--ink); line-height: 1;
  }
  .title .brand { color: var(--white); }
  .hero-child {
    position: absolute; left: 95px; top: 175px; width: 150px; height: 600px;
    border-radius: 70px 70px 30px 30px;
    background: linear-gradient(180deg, rgba(58,74,110,0.85) 0%, rgba(42,58,94,0.8) 60%, rgba(30,42,70,0.8) 100%);
  }
  .headline {
    position: absolute; left: 320px; width: 550px; text-align: center;
    font-family: 'Quicksand', Arial, sans-serif; font-weight: 700; font-size: 44px; line-height: 1;
  }
  .headline.lead { top: 222px; color: var(--orange); }
  .headline.sub { top: 283px; color: var(--white); }
  .features-tag {
    position: absolute; left: 464px; top: 368px; width: 238px; height: 43px; border-radius: 22px;
    background: linear-gradient(90deg, var(--orange-deep), var(--orange-light), var(--orange-deep));
    font-family: 'Quicksand', Arial, sans-serif; font-weight: 600; font-size: 27px;
    color: var(--ink); text-align: center; line-height: 43px;
  }
  .feature-list { position: absolute; list-style: none; }
  .feature-list li {
    position: relative; padding-left: 32px; height: 49px;
    font-style: italic; font-weight: 900; font-size: 25px; color: var(--white);
  }
  .feature-list li::before {
    content: ""; position: absolute; left: 0; top: 8px; width: 17px; height: 17px;
    border-radius: 50%; background: var(--orange);
  }
  .feature-list.col-a { left: 318px; top: 460px; }
  .feature-list.col-b { left: 553px; top: 462px; }
  .web-pill {
    position: absolute; left: 335px; top: 562px; width: 495px; height: 60px;
  }
  .web-pill .shadow-ring {
    position: absolute; left: 4px; top: 5px; right: -4px; bottom: -5px;
    border: 3px solid var(--orange); border-radius: 30px;
  }
  .web-pill .ring {
    position: absolute; inset: 0; border: 3px solid var(--white); border-radius: 30px;
    font-family: 'Quicksand', Arial, sans-serif; font-weight: 600; font-size: 25px;
    text-align: center; line-height: 53px; color: var(--white);
  }
  .web-pill .lead-in { color: var(--orange); }
  .mum-photo {
    position: absolute; left: 372px; top: 648px; width: 92px; height: 128px;
    border-radius: 46px 46px 0 0;
    background: linear-gradient(180deg, rgba(217,184,154,0.8) 0%, rgba(232,80,106,0.85) 55%, rgba(224,65,93,0.85) 100%);
  }
  .mum-note {
    position: absolute; left: 490px; top: 716px;
    font-style: italic; font-weight: 700; font-size: 25px; color: var(--white);
  }
  .snapshot {
    position: absolute; background: var(--white); padding: 8px;
    box-shadow: 0 4px 12px rgba(0,0,0,0.45);
  }
  .snapshot .photo { width: 100%; height: 100%; }
  .snapshot.one { left: 918px; top: 170px; width: 236px; height: 186px; transform: rotate(3deg); }
  .snapshot.one .photo { background: linear-gradient(180deg, #f7f7f7, #e6eaf0); }
  .snapshot.two { left: 942px; top: 360px; width: 214px; height: 182px; transform: rotate(-2deg); }
  .snapshot.two .photo { background: linear-gradient(180deg, var(--sky), #7ea2de); }
  .snapshot.three { left: 910px; top: 560px; width: 244px; height: 192px; transform: rotate(4deg); }
  .snapshot.three .photo { background: linear-gradient(180deg, #a2c1f2, #84a9e3); }
  .tape { position: absolute; width: 68px; height: 22px; opacity: 0.9; }
  .tape.t1 { left: 1090px; top: 150px; background: var(--tape); transform: rotate(28deg); }
  .tape.t2 { left: 920px; top: 350px; background: var(--tape-dark); transform: rotate(-28deg); }
  .tape.t3 { left: 918px; top: 548px; background: var(--tape); transform: rotate(30deg); }
  .footer {
    position: absolute; left: 0; top: 776px; width: 1200px; height: 126px; background: var(--white);
  }
  .contact { position: absolute; display: flex; align-items: center; color: var(--ink); font-weight: 700; }
  .contact.phone { left: 55px; top: 55px; font-size: 29px; gap: 14px; }
  .contact.address { left: 330px; top: 44px; font-size: 20px; gap: 10px; align-items: flex-start; line-height: 25px; }
  .social { position: absolute; left: 602px; top: 60px; display: flex; align-items: center; gap: 16px; }
  .social .label { font-weight: 700; font-size: 19px; color: var(--orange); margin-right: 6px; }
  .social .dot { width: 23px; height: 23px; border-radius: 50%; background: var(--ink); }
  .wordmark {
    position: absolute; left: 908px; top: 42px; width: 220px; text-align: center;
    font-family: 'Quicksand', Arial, sans-serif; font-weight: 500; font-size: 52px;
    color: var(--grey-text); letter-spacing: 1px; line-height: 1;
  }
</style>
</head>
<body>
<main class="flyer">
  <svg class="backdrop" width="1200" height="902" viewBox="0 0 1200 902" aria-hidden="true">
    <defs>
      <radialGradient id="stage-glow" cx="0.5" cy="0.5" r="0.6">
        <stop offset="0" stop-color="#3d3d3d"/>
        <stop offset="1" stop-color="#262626"/>
      </radialGradient>
    </defs>
    <path d="M0 268 C 260 175, 650 120, 1200 262 L1200 756 L0 756 Z" fill="url(#stage-glow)"/>
    <path d="M0 268 C 260 175, 650 120, 1200 262" fill="none" stroke="#ffffff" stroke-width="3"/>
    <rect x="0" y="756" width="1200" height="20" fill="var(--orange)"/>
  </svg>

  <h1 class="title"><span class="brand">LUMORA</span> KIDS CLOTHING</h1>

  <div class="hero-child" role="img" aria-label="Boy wearing a navy hooded top with striped sleeves and navy pants"></div>

  <p class="headline lead">OUR CHILDREN’S SKIN IS</p>
  <p class="headline sub">SO SOFT AND DELICATE</p>

  <div class="features-tag">FEATURES</div>
  <ul class="feature-list col-a">
    <li>High necklines</li>
    <li>Long sleeves</li>
  </ul>
  <ul class="feature-list col-b">
    <li>Thumb loops for hand cover</li>
    <li>Breathable fabrics</li>
  </ul>

  <div class="web-pill">
    <span class="shadow-ring"></span>
    <p class="ring"><span class="lead-in">See more at</span> www.lumora-wear.com</p>
  </div>

  <div class="mum-photo" role="img" aria-label="Woman wearing a coral pink wrap top"></div>
  <p class="mum-note">WE have things for Mum as well</p>

  <figure class="snapshot one"><div class="photo" role="img" aria-label="Girl in a light blue long-sleeve top against a white wall"></div></figure>
  <figure class="snapshot two"><div class="photo" role="img" aria-label="Three children in sun hats and long sleeves against a blue backdrop"></div></figure>
  <figure class="snapshot three"><div class="photo" role="img" aria-label="Three children in pastel outfits holding balloons"></div></figure>
  <span class="tape t1"></span>
  <span class="tape t2"></span>
  <span class="tape t3"></span>

  <footer class="footer">
    <p class="contact phone">
      <svg width="24" height="24" viewBox="0 0 24 24" aria-hidden="true"><circle cx="12" cy="12" r="10.5" fill="none" stroke="#1f1f1f" stroke-width="1.8"/><path d="M8.5 6.5 L10.5 9 L9.3 10.5 C10 12.2 11.6 13.9 13.4 14.7 L14.9 13.5 L17.4 15.4 L16.3 17.4 C11.8 17.3 6.8 12.3 6.6 7.7 Z" fill="#1f1f1f"/></svg>
      03 5550 1472
    </p>
    <p class="contact address">
      <svg width="16" height="16" viewBox="0 0 16 16" aria-hidden="true" style="margin-top:3px"><path d="M8 1 L15 8 L13 8 L13 15 L9.5 15 L9.5 10.5 L6.5 10.5 L6.5 15 L3 15 L3 8 L1 8 Z" fill="#1f1f1f"/></svg>
      <span>18 Fernleigh Rd<br>Maple East Vic 3999</span>
    </p>
    <div class="social">
      <span class="label">Follow us on</span>
      <span class="dot"></span><span class="dot"></span><span class="dot"></span><span class="dot"></span>
    </div>
    <p class="wordmark">LUMORA</p>
  </footer>
</main>
</body>
</html>
```